PEACFUL ACUPUNCTURE PRACTITIONER NEEDS A NEW COAT

I need a new design for an exiting website http://willowgateneedlework.com/ for a acupuncturist. This will be a minimalism design with lots and lots of white space. Home page and one interior page. Please keep the feeling of calm and peaceful serenity. For Color scheme: https://www.morningfernclinic.com/fertility. The bottom part of the home page with sections and links to the service pages: https://harborlotuswellness.com/. The client likes this the best: http://mfclinic.com/. I'm attaching the logo and content pages.

Target Market(s)

Women

Industry/Entity Type

Wellness, health, wellbeing, meditation

Number of Pages Required

2 page

Font styles to use
Sans Serif
Decorative

Colors

Designer to choose colors to be used in the design.

Requirements
Must have
Nice to have
• Follow new website drafts and links
Should not have
• Busy with bright colors. No poping

```html
<!DOCTYPE html>
<html lang="en">
<head>
<meta charset="utf-8">
<title>Willowgate Acupuncture</title>
<link href="https://fonts.googleapis.com/css2?family=Bitter:wght@400;500&family=Mulish:wght@400&family=Roboto+Condensed:wght@400&display=swap" rel="stylesheet">
<style>
:root{
  --ink:#555459;
  --body:#3a3a3a;
  --rose:#c08d96;
  --rose-soft:#e4cfd4;
  --slate:#a7b4c5;
  --card-line:#f3eee4;
  --footer-bg:#f8f4f5;
  --rule:#e2dfe2;
  --white:#ffffff;
}
*{margin:0;padding:0;box-sizing:border-box}
html,body{width:670px;height:1200px;overflow:hidden;background:var(--white)}
body{position:relative;font-family:'Mulish',sans-serif;color:var(--body)}
.abs{position:absolute}
.serif{font-family:'Bitter',serif}

/* header */
.brand{left:0;width:670px;top:6px;text-align:center;color:var(--ink);font-family:'Bitter',serif;font-weight:400}
.brand-name{font-size:21px;line-height:24px;letter-spacing:.3px}
.brand-sub{font-size:11px;letter-spacing:3.5px;line-height:12px}
.nav-rule{left:0;width:670px;height:1px;background:var(--rule)}
.main-nav{top:51px;left:0;width:670px;height:21px}
.main-nav a{position:absolute;top:0;height:21px;line-height:21px;font-family:'Bitter',serif;font-size:7.6px;color:var(--ink);text-decoration:none;white-space:nowrap}
.main-nav a.is-current{background:var(--slate);color:var(--white);padding:0 4px}

/* hero */
.hero{top:80px;left:0;width:670px;height:275px;background:linear-gradient(180deg,#e9e4e0 0%,#d9c2b0 35%,#b89680 60%,#5a4d48 85%,#2d2a2a 100%)}
.hero-title{top:284px;left:0;width:670px;text-align:center;font-family:'Roboto Condensed',sans-serif;font-size:23px;line-height:32px;color:var(--white)}

/* philosophy */
.section-title{font-family:'Bitter',serif;font-weight:400;color:var(--ink);font-size:22px;line-height:26px}
.philosophy-title{top:399px;left:65px}
.philosophy-text{top:433px;left:67px;width:350px;font-size:8.3px;line-height:16.9px;color:var(--body)}
.philosophy-text p+p{margin-top:2px}
.philosophy-mark{left:438px;top:392px;width:150px;height:150px;border-radius:50%;background:var(--rose-soft)}

/* focus */
.focus-title{top:581px;left:0;width:670px;text-align:center}
.card{top:624px;width:133px;height:186px;border:1px solid var(--card-line);text-align:center}
.card-photo{position:absolute;left:33px;top:17px;width:66px;height:66px;border-radius:50%;border:2px solid #f0e4d4}
.card-title{position:absolute;top:95px;left:0;width:100%;font-family:'Bitter',serif;font-size:9.6px;color:var(--rose)}
.card-text{position:absolute;top:113px;left:6px;right:6px;font-size:7.5px;line-height:13.8px;color:var(--body)}
.card-arrow{position:absolute;left:60px;top:166px}

/* cta */
.cta-title{top:845px;left:0;width:670px;text-align:center}
.cta-text{top:878px;left:70px;width:530px;text-align:center;font-size:8.9px;line-height:17px}
.cta-button{left:266px;top:916px;width:137px;height:25px;background:var(--slate);color:var(--body);font-size:9.3px;line-height:25px;text-align:center}
.cta-button svg{vertical-align:middle;margin-right:6px;margin-top:-2px}

/* footer */
.footer-shape{left:0;top:980px}
.footer-badge{left:307px;top:962px;width:56px;height:56px;border-radius:50%;background:var(--white)}
.footer-brand{top:1022px}
.footer-brand .brand-name{font-size:20px}
.footer-nav{top:1076px;left:0;width:670px;height:18px}
.footer-nav a{position:absolute;top:0;font-family:'Bitter',serif;font-size:7.6px;color:var(--ink);text-decoration:none;white-space:nowrap}
.footer-rule{left:65px;width:550px;height:1px;background:var(--rule)}
.contact-icon{width:27px;height:27px;border-radius:50%;border:1px solid #d7d5da;background:var(--white);display:flex;align-items:center;justify-content:center}
.contact-label{font-family:'Bitter',serif;font-weight:500;font-size:7.8px;color:var(--ink)}
.contact-value{font-family:'Bitter',serif;font-size:7.8px;color:var(--ink);margin-top:3px}
.copyright{top:1173px;left:0;width:670px;text-align:center;font-family:'Bitter',serif;font-size:7.6px;color:var(--ink)}
</style>
</head>
<body>

<header>
  <div class="abs brand">
    <div class="brand-name">Willowgate</div>
    <div class="brand-sub">ACUPUNCTURE</div>
  </div>
  <div class="abs nav-rule" style="top:51px"></div>
  <nav class="abs main-nav">
    <a class="is-current" style="left:65px">Home</a>
    <a style="left:104px">About</a>
    <a style="left:138px">Fertility &amp; Pregnancy</a>
    <a style="left:225px">Hormone Balance</a>
    <a style="left:302px">Strength &amp; Structure</a>
    <a style="left:388px">Emotional Wellbeing</a>
    <a style="left:474px">Online Shop</a>
    <a style="left:530px">Testimonials</a>
    <a style="left:588px">Contact</a>
  </nav>
  <div class="abs nav-rule" style="top:72px"></div>
</header>

<section>
  <div class="abs hero" role="img" aria-label="Practitioner's hand placing acupuncture needles in a woman's back"></div>
  <h1 class="abs hero-title" style="font-weight:400">Our Goal Is To Help Every Woman Develop A Deeper<br>Sense of Communication With Her Body.</h1>
</section>

<section>
  <h2 class="abs section-title philosophy-title">Philosophy of Care</h2>
  <div class="abs philosophy-text">
    <p>Acupuncture &amp; Chinese Herbal Medicine are rooted in over 3000 years of history and tradition. As a complete medical system that has remained flexible and relevant we honor what has worked from the past while embracing the medicine of tomorrow.</p>
    <p>At Willowgate Acupuncture we provide compassionate, respectful and empowering care in a safe and inclusive environment. Our goal is to harmonize physical, mental and emotional wellbeing to strengthen the Willowgate from which we all strive to live.</p>
  </div>
  <div class="abs philosophy-mark" aria-hidden="true"></div>
</section>

<section>
  <h2 class="abs section-title focus-title">Areas of Focus</h2>

  <article class="abs card" style="left:65px">
    <div class="card-photo" role="img" aria-label="Bird's nest among green leaves" style="background:#5f7048"></div>
    <h3 class="card-title" style="font-weight:400">Fertility &amp; Pregnancy</h3>
    <p class="card-text">Lorem ipsum dolor sidfat amet, consectetuer adipiscing elit, sed diam nonummy nibh.</p>
    <svg class="card-arrow" width="11" height="6" viewBox="0 0 11 6"><path d="M0 3H9M7 1L10 3L7 5" stroke="#c08d96" stroke-width="1.2" fill="none"/></svg>
  </article>

  <article class="abs card" style="left:206px">
    <div class="card-photo" role="img" aria-label="Balanced stones against sea and sky" style="background:linear-gradient(180deg,#4a86c9 0%,#7fb0dc 55%,#c57a4f 70%,#4f7fb8 100%)"></div>
    <h3 class="card-title" style="font-weight:400">Emotional&nbsp; Wellbeing</h3>
    <p class="card-text">Lorem ipsum dolor sidfat amet, consectetuer adipiscing elit, sed diam nonummy nibh.</p>
    <svg class="card-arrow" width="11" height="6" viewBox="0 0 11 6"><path d="M0 3H9M7 1L10 3L7 5" stroke="#c08d96" stroke-width="1.2" fill="none"/></svg>
  </article>

  <article class="abs card" style="left:343px">
    <div class="card-photo" role="img" aria-label="Stacked pebbles on a large rock by the sea" style="background:linear-gradient(180deg,#5b8fd0 0%,#8ab4e0 50%,#9a8d80 75%,#4c6f9a 100%)"></div>
    <h3 class="card-title" style="font-weight:400">Hormone Balance</h3>
    <p class="card-text">Lorem ipsum dolor sidfat amet, consectetuer adipiscing elit, sed diam nonummy nibh.</p>
    <svg class="card-arrow" width="11" height="6" viewBox="0 0 11 6"><path d="M0 3H9M7 1L10 3L7 5" stroke="#c08d96" stroke-width="1.2" fill="none"/></svg>
  </article>

  <article class="abs card" style="left:483px">
    <div class="card-photo" role="img" aria-label="Single large tree in a field under blue sky" style="background:linear-gradient(180deg,#7fa6d8 0%,#3f5a2c 45%,#2f4520 75%,#6f8a4a 100%)"></div>
    <h3 class="card-title" style="font-weight:400">Strength &amp; Structure</h3>
    <p class="card-text">Lorem ipsum dolor sidfat amet, consectetuer adipiscing elit, sed diam nonummy nibh.</p>
    <svg class="card-arrow" width="11" height="6" viewBox="0 0 11 6"><path d="M0 3H9M7 1L10 3L7 5" stroke="#c08d96" stroke-width="1.2" fill="none"/></svg>
  </article>
</section>

<section>
  <h2 class="abs section-title cta-title">Acupuncture Can Help!</h2>
  <p class="abs cta-text">Schedule A Free 30 Minute ConsultationConsultations are always available to help answer any questions you may have about acupuncture or herbal medicine in a relaxed environment.</p>
  <div class="abs cta-button">
    <svg width="13" height="13" viewBox="0 0 24 24"><path d="M6 3l3 4-2 2c1 3 4 6 7 7l2-2 4 3-2 3C10 20 4 14 3 5z" fill="none" stroke="#3a3a3a" stroke-width="1.4"/></svg>Call Us: 413-555-0142
  </div>
</section>

<footer>
  <svg class="abs footer-shape" width="670" height="220" viewBox="0 0 670 220">
    <path d="M0 61 Q335 -33 670 60 L670 220 L0 220 Z" fill="#f8f4f5"/>
    <path d="M40 49 Q335 -33 670 60" fill="none" stroke="#a7b4c5" stroke-width="2.5"/>
  </svg>
  <div class="abs footer-badge"></div>
  <div class="abs brand footer-brand">
    <div class="brand-name">Willowgate</div>
    <div class="brand-sub">ACUPUNCTURE</div>
  </div>
  <nav class="abs footer-nav">
    <a style="left:66px">Home</a>
    <a style="left:101px">About</a>
    <a style="left:135px">Fertility &amp; Pregnancy</a>
    <a style="left:222px">Hormone Balance</a>
    <a style="left:299px">Strength &amp; Structure</a>
    <a style="left:385px">Emotional Wellbeing</a>
    <a style="left:471px">Online Shop</a>
    <a style="left:527px">Testimonials</a>
    <a style="left:585px">Contact</a>
  </nav>
  <div class="abs footer-rule" style="top:1108px"></div>

  <div class="abs contact-icon" style="left:65px;top:1130px">
    <svg width="11" height="13" viewBox="0 0 12 14"><path d="M6 13C3 9 1.5 7 1.5 5a4.5 4.5 0 019 0c0 2-1.5 4-4.5 8z" fill="none" stroke="#7a7a80" stroke-width=".9"/><circle cx="6" cy="5" r="1.5" fill="none" stroke="#7a7a80" stroke-width=".9"/></svg>
  </div>
  <div class="abs" style="left:101px;top:1132px">
    <div class="contact-label">Willowgate Acupuncture</div>
    <div class="contact-value">14 Alder Row | Easthampton MA</div>
  </div>

  <div class="abs contact-icon" style="left:294px;top:1130px">
    <svg width="12" height="12" viewBox="0 0 24 24"><path d="M6 3l3 4-2 2c1 3 4 6 7 7l2-2 4 3-2 3C10 20 4 14 3 5z" fill="none" stroke="#7a7a80" stroke-width="1.5"/></svg>
  </div>
  <div class="abs" style="left:326px;top:1131px">
    <div class="contact-label">Call Us</div>
    <div class="contact-value">413-555-0142</div>
  </div>

  <div class="abs contact-icon" style="left:446px;top:1130px">
    <svg width="12" height="11" viewBox="0 0 14 12"><path d="M1 4h12v7H1z M1 4l6 4 6-4 M3 4V1h8v3" fill="none" stroke="#7a7a80" stroke-width=".9"/></svg>
  </div>
  <div class="abs" style="left:481px;top:1131px">
    <div class="contact-label">Email Us</div>
    <div class="contact-value">hello@willowgateneedlework.com</div>
  </div>

  <div class="abs footer-rule" style="top:1168px"></div>
  <p class="abs copyright">Copyright © 2021 Willowgate Acupuncture. All Rights Reserved.</p>
</footer>

</body>
</html>
```